VANTA SWEEP

Need a professional looking business card that can fit : Name, Title, Cell, and office phone numbers. On the flip side we would like a list of our services : Highway accident management and towing, Crime scene clean up, Illegal drug lab clean up, Drug disposal, and Hazardous materials clean up.

```html
<!DOCTYPE html>
<html lang="en">
<head>
<meta charset="UTF-8">
<title>Vanta Sweep – Services Card</title>
<link rel="stylesheet" href="https://fonts.googleapis.com/css2?family=Quicksand:wght@300&display=swap">
<style>
  :root {
    --card-green: #2b8c57;
    --badge-teal: #1d5b5f;
    --text-white: #ffffff;
  }
  html, body {
    margin: 0;
    padding: 0;
    width: 1200px;
    height: 702px;
    overflow: hidden;
    background: var(--card-green);
  }
  .card-back {
    position: relative;
    width: 1200px;
    height: 702px;
    background: var(--card-green);
    font-family: "Quicksand", sans-serif;
    font-weight: 300;
    color: var(--text-white);
  }
  .service-list {
    position: absolute;
    left: 83px;
    top: 57px;
    margin: 0;
    padding: 0;
    list-style: none;
  }
  .service-item {
    font-size: 45px;
    line-height: 110.5px;
    letter-spacing: 2.6px;
    white-space: nowrap;
  }
  .brand-mark {
    position: absolute;
    left: 708px;
    top: 153px;
    width: 412px;
    height: 412px;
  }
  .brand-disc {
    fill: var(--badge-teal);
  }
  .brand-name {
    position: absolute;
    left: 708px;
    top: 153px;
    width: 412px;
    height: 412px;
    display: flex;
    align-items: center;
    justify-content: center;
    font-size: 44px;
    letter-spacing: 3px;
    color: var(--text-white);
    white-space: nowrap;
  }
</style>
</head>
<body>
  <main class="card-back">
    <ul class="service-list">
      <li class="service-item">Highway accident management and towing</li>
      <li class="service-item">Crime scene clean up</li>
      <li class="service-item">Illegal drug lab clean up</li>
      <li class="service-item">Drug disposal</li>
      <li class="service-item">Hazardous materials clean up</li>
    </ul>
    <svg class="brand-mark" viewBox="0 0 412 412" aria-hidden="true">
      <circle class="brand-disc" cx="206" cy="206" r="206"/>
    </svg>
    <div class="brand-name">VANTA SWEEP</div>
  </main>
</body>
</html>
```